Upmarket Food Product Website (Maple Syrup)

I want an upmarket looking website designed for our maple syrup products which are the best of the best. This website will be to promote the brand only and will not take any orders through it. Therefore the design has to be similar in feel to the examples shown below for both Maple Syrup and Whiskey producers.

https://www.ridgeleafsyrup.com/ (Like this design we will want a similar design)
https://brackenvale.com/us/ (Like the design and colour scheme which goes along with the Maple leaf colours of orange and brown)
http://uk.thehollowmere.com/ (Another good website design)

We have a logo already which we want to keep however if this logo needs to be darker or textured to give it a more upmarket feel then its fine to play around with this can be found in the attachments.

Target Market(s)

US and Canada

Industry/Entity Type

Product

Contact Information for Business Card

President: Neil Parrish
Bramblewick Maple (Quality Maple Syrup)
Tel: (+1) 506-247-8135
Web: www.bramblewickmaple.com
Email: info@bramblewickmaple.com

Coding

Coded - Design and coding required

Number of Pages Required

5+ page

Font styles to use
Sans Serif

Requirements
Must have
• A quality feel, this product is an expensive brand product and as such the website design needs to convey this effectively.
• Must allow for text boxes on each page allowing for 500 words of text to be added at a later stage to each page.
Nice to have
• A similar colour scheme to the logo supplied however the logo may be toned down to darker colours as its a bit bright
Should not have
• Any shopping section or prices for products shown. This site is to build the brand identity and will not offer syrups for sale directly

```html
<!DOCTYPE html>
<html lang="en">
<head>
<meta charset="utf-8">
<title>Bramblewick Maple</title>
<link href="https://fonts.googleapis.com/css2?family=Open+Sans:wght@400;600;700&display=swap" rel="stylesheet">
<style>
:root{
  --orange:#f07a12;
  --orange-dark:#d9650a;
  --green:#3f8f2a;
  --green-dark:#2f7220;
  --brown:#5a3516;
  --beige:#efe9dc;
  --text:#6b6b6b;
  --dark:#2b2b2b;
  --white:#ffffff;
}
*{margin:0;padding:0;box-sizing:border-box}
html,body{width:700px;height:1200px;overflow:hidden}
body{font-family:"Open Sans",Arial,sans-serif;color:var(--text);background:var(--white);position:relative}
.site-header{height:34px;background:var(--white);position:relative;border-bottom:1px solid #eee;z-index:3}
.nav{display:flex;align-items:center;height:34px;font-size:7px;color:#777;position:absolute;top:0}
.nav a{color:inherit;text-decoration:none;margin-right:22px;display:flex;align-items:center;gap:4px}
.nav a::before{content:"";width:5px;height:5px;border-radius:50%;background:#d8cfc0}
.nav a.active{color:var(--orange)}
.nav-left{left:58px}
.nav-right{left:430px}
.brand{position:absolute;left:300px;top:0;width:100px;height:70px;background:var(--white);border-radius:0 0 50px 50px;box-shadow:0 2px 5px rgba(0,0,0,.15);display:flex;flex-direction:column;align-items:center;justify-content:center;gap:4px;z-index:4}
.brand-dot{width:18px;height:18px;border-radius:50%;background:var(--orange)}
.brand-name{font-size:9px;font-weight:700;color:var(--brown);text-align:center;line-height:1.1}
.hero{height:340px;position:relative;background:linear-gradient(100deg,#b9a996 0%,#8a6a45 30%,#c7893a 50%,#8e5a22 65%,#c2b39f 100%)}
.hero-caption{position:absolute;left:0;top:186px;width:225px}
.hero-title{background:rgba(20,20,20,.75);color:var(--white);font-size:14px;font-weight:600;padding:9px 14px}
.hero-sub{background:var(--green);color:#e6f1df;font-size:6.5px;line-height:1.5;padding:6px 14px}
.intro{height:174px;position:relative}
.intro-photo{position:absolute;left:58px;top:22px;width:245px;height:128px;background:radial-gradient(circle at 40% 40%,#e9a63a,#b3621a 60%,#7a3c10)}
.intro-text{position:absolute;left:330px;top:20px;width:320px}
.intro-text h2{color:var(--orange);font-size:10.5px;font-weight:600;line-height:1.35;margin-bottom:8px}
.intro-text p{font-size:6.5px;line-height:1.6;margin-bottom:6px}
.highlights{height:280px;background:var(--beige);position:relative}
.press{position:absolute;left:58px;top:24px;width:290px}
.highlights h3{font-size:10px;font-weight:600;color:#555;margin-bottom:12px}
.press-cards{display:flex;gap:24px}
.press-card{width:125px}
.press-photo{height:72px;position:relative;margin-bottom:8px}
.press-photo.bottle{background:linear-gradient(160deg,#f6f2ea,#e0b56a 55%,#b56d1c)}
.press-photo.stack{background:linear-gradient(160deg,#f4eee4,#d08a3a 55%,#8a4a16)}
.tag{position:absolute;right:0;top:0;background:var(--orange);color:var(--white);font-size:5.5px;padding:3px 5px}
.card-title{color:var(--green);font-size:7px;font-weight:600;margin-bottom:4px}
.card-text{font-size:6px;line-height:1.55;margin-bottom:8px}
.btn{display:inline-block;background:var(--green);color:var(--white);font-size:5.5px;padding:4px 10px;border-radius:2px}
.recognitions{position:absolute;left:400px;top:24px;width:250px}
.award{display:flex;gap:12px;margin-bottom:20px}
.award-icon{flex:none;width:34px;height:34px;border-radius:50%;background:var(--orange);display:flex;align-items:center;justify-content:center}
.stars{display:flex;gap:2px;margin-bottom:6px}
.innovation{height:230px;padding:44px 75px 0;text-align:center}
.innovation h3{color:var(--orange);font-size:10px;font-weight:600;margin-bottom:14px}
.innovation p{font-size:6.5px;line-height:1.7;margin-bottom:14px}
.site-footer{height:110px;background:var(--orange);position:relative;color:var(--white)}
.footer-col{position:absolute;top:16px}
.footer-col h4{font-size:7px;font-weight:700;letter-spacing:.5px;margin-bottom:10px}
.contact-line{display:flex;align-items:center;gap:6px;font-size:6px;margin-bottom:6px}
.newsletter-input{width:110px;height:16px;background:var(--white);color:#999;font-size:6px;padding:4px 6px;margin-bottom:6px}
.social{display:flex;gap:6px}
.social span{width:18px;height:18px;border-radius:50%;background:rgba(255,255,255,.3)}
.copyright{height:32px;background:var(--dark);color:#bbb;font-size:6px;display:flex;align-items:center;justify-content:center}
</style>
</head>
<body>
<header class="site-header">
  <nav class="nav nav-left"><a class="active">Home</a><a>About Bramblewick Maple</a><a>Our Syrups</a></nav>
  <nav class="nav nav-right"><a>Recipes</a><a>Apply To Become A Retailer</a></nav>
  <div class="brand"><span class="brand-dot"></span><span class="brand-name">Bramblewick<br>Maple</span></div>
</header>

<section class="hero" role="img" aria-label="Photograph of maple leaf shaped syrup bottles on a table">
  <div class="hero-caption">
    <div class="hero-title">Pure Canadian Maple Syrup</div>
    <div class="hero-sub">Harvested from Canadian forests and boiled<br>slowly for rich flavour.</div>
  </div>
</section>

<section class="intro">
  <div class="intro-photo" role="img" aria-label="Photograph of syrup dripping from a dipper into a bowl"></div>
  <div class="intro-text">
    <h2>Bramblewick Maple - Setting The Standard For Pure Canadian Maple Syrup</h2>
    <p>Bramblewick Maple makes pure maple syrup from old sugar maples in New Brunswick. Every batch is tapped by hand, boiled over wood and graded with care so each bottle carries a clean, deep taste.</p>
    <p>Our small family team follows the seasons closely, collecting sap only on the best days of spring. The result is a syrup with a smooth body and warm caramel notes that suits breakfast, baking and fine dining alike.</p>
  </div>
</section>

<section class="highlights">
  <div class="press">
    <h3>Bramblewick Maple In The Press</h3>
    <div class="press-cards">
      <article class="press-card">
        <div class="press-photo bottle" role="img" aria-label="Photograph of a syrup bottle"><span class="tag">11 Jun</span></div>
        <div class="card-title">Maple syrup wins praise</div>
        <p class="card-text">Our amber syrup was featured in a regional food guide this spring.</p>
        <span class="btn">Read more</span>
      </article>
      <article class="press-card">
        <div class="press-photo stack" role="img" aria-label="Photograph of pancakes with syrup"><span class="tag">02 May</span></div>
        <div class="card-title">Chefs choose our syrup</div>
        <p class="card-text">Local restaurants now pour our dark syrup over seasonal desserts.</p>
        <span class="btn">Read more</span>
      </article>
    </div>
  </div>
  <div class="recognitions">
    <h3>Recognitions</h3>
    <div class="award">
      <div class="award-icon"><svg width="16" height="16" viewBox="0 0 24 24"><path fill="#fff" d="M12 2l3 6.5 7 .8-5.2 4.8 1.5 7L12 17.6 5.7 21.1l1.5-7L2 9.3l7-.8z"/></svg></div>
      <div>
        <div class="card-title">Awarded best amber syrup</div>
        <p class="card-text">Recognised by a national tasting panel for its depth and clarity of flavour.</p>
        <div class="stars"><svg width="40" height="7" viewBox="0 0 40 7"><g fill="var(--orange)"><circle cx="3.5" cy="3.5" r="3"/><circle cx="11.5" cy="3.5" r="3"/><circle cx="19.5" cy="3.5" r="3"/><circle cx="27.5" cy="3.5" r="3"/><circle cx="35.5" cy="3.5" r="3"/></g></svg></div>
        <span class="btn">Read more</span>
      </div>
    </div>
    <div class="award">
      <div class="award-icon"><svg width="16" height="16" viewBox="0 0 24 24"><path fill="#fff" d="M12 2l3 6.5 7 .8-5.2 4.8 1.5 7L12 17.6 5.7 21.1l1.5-7L2 9.3l7-.8z"/></svg></div>
      <div>
        <div class="card-title">Gold medal for dark syrup</div>
        <p class="card-text">Honoured at a fine food fair for a rich, balanced and natural taste.</p>
        <div class="stars"><svg width="40" height="7" viewBox="0 0 40 7"><g fill="var(--orange)"><circle cx="3.5" cy="3.5" r="3"/><circle cx="11.5" cy="3.5" r="3"/><circle cx="19.5" cy="3.5" r="3"/><circle cx="27.5" cy="3.5" r="3"/><circle cx="35.5" cy="3.5" r="3"/></g></svg></div>
        <span class="btn">Read more</span>
      </div>
    </div>
  </div>
</section>

<section class="innovation">
  <h3>Innovation</h3>
  <p>We pair old sugaring traditions with careful modern methods. Clean tubing, gentle evaporation and strict filtering keep every drop pure, while our grading lab checks colour, density and taste before any syrup is sealed in glass and sent out to our retail partners across the country.</p>
  <p>Each season we study our forest, plant young maples and measure sap quality so the trees stay healthy for generations. This patient approach lets us offer a syrup that is both honest to its roots and worthy of the finest tables in North America.</p>
</section>

<footer class="site-footer">
  <div class="footer-col" style="left:58px">
    <h4>CONTACT US</h4>
    <div class="contact-line"><svg width="8" height="8" viewBox="0 0 24 24"><path fill="#fff" d="M12 2a7 7 0 00-7 7c0 5 7 13 7 13s7-8 7-13a7 7 0 00-7-7zm0 9.5A2.5 2.5 0 1112 6.5a2.5 2.5 0 010 5z"/></svg>12 Orchard Lane, Sussex, New Brunswick</div>
    <div class="contact-line"><svg width="8" height="8" viewBox="0 0 24 24"><path fill="#fff" d="M6.6 10.8a15 15 0 006.6 6.6l2.2-2.2a1 1 0 011-.25 11.4 11.4 0 003.6.57 1 1 0 011 1V20a1 1 0 01-1 1A17 17 0 013 4a1 1 0 011-1h3.5a1 1 0 011 1c0 1.25.2 2.45.57 3.57a1 1 0 01-.25 1z"/></svg>(+1) 506-247-8135</div>
    <div class="contact-line"><svg width="8" height="8" viewBox="0 0 24 24"><path fill="#fff" d="M3 5h18v14H3z M3 5l9 7 9-7" stroke="#f07a12" stroke-width="1.5"/></svg>info@bramblewickmaple.com</div>
  </div>
  <div class="footer-col" style="left:300px">
    <h4>NEWSLETTER</h4>
    <div class="newsletter-input">Enter your e-mail</div>
    <span class="btn">Submit</span>
  </div>
  <div class="footer-col" style="left:530px">
    <h4>FOLLOW WITH US</h4>
    <div class="social"><span></span><span></span><span></span><span></span><span></span></div>
  </div>
</footer>
<div class="copyright">© Bramblewick Maple 2015 | All Rights Reserved</div>
</body>
</html>
```